Bright Harbor Capital website

Build a website template for the Bright Harbor Capital fund.
Looking for a cool website design showing companies we are using the latest in web design trends. We want to attract app developers, typically the younger set.
A good example of one of our competitive firms is http://tallmeadowfund.example
The required components for the website include:
1) Funding application
2) about our firm
a) Partner profiles - We will include photographs and bios about each of the partners in our firm.
b) Invest with Bright Harbor - This will include information how to invest with our fund
c) our process - About our process for evaluating, funding and helping build successful businesses - This will include a narrative about the target companies, how we work, the type of deals we are interested in, our expectations, etc ...
3) Investment profiles - Stories about the companies we invest with
4) News - Output from our twitter feed and copies of our Blog posts

```html
<!DOCTYPE html>
<html lang="en">
<head>
<meta charset="utf-8">
<title>Bright Harbor Capital</title>
<link href="https://fonts.googleapis.com/css2?family=Open+Sans:ital,wght@0,300;0,400;0,600;0,700;1,400&family=Cinzel:wght@400;600&display=swap" rel="stylesheet">
<style>
:root{
  --green:#4c9e3e;
  --green-text:#5a9a3a;
  --green-dark:#3e8e34;
  --grey-line:#8a8a8a;
  --text:#444;
  --muted:#666;
  --panel:#e8e8e8;
  --footer-top:#7c7c7c;
  --footer-bottom:#575757;
  --footer-bar:#3b3b3b;
  --white:#fff;
}
*{box-sizing:border-box;margin:0;padding:0}
html,body{width:1200px;height:1191px;overflow:hidden;background:#fff}
body{position:relative;font-family:Arial,Helvetica,sans-serif;color:var(--text)}
.abs{position:absolute}

.brand{left:100px;top:14px;display:flex;align-items:center;gap:12px}
.brand-dot{width:58px;height:58px;border-radius:50%;background:var(--green-text)}
.brand-name{font-family:'Open Sans',sans-serif;font-weight:600;font-size:27px;color:var(--green-text)}

.contact{top:28px;left:696px;display:flex;align-items:center;font-family:'Open Sans',sans-serif;font-size:15px;color:#555}
.contact .phone{margin-left:8px;letter-spacing:.5px}
.contact .sep{margin:0 20px;color:#777}
.contact .follow{font-weight:600;color:#555;margin-right:12px}
.social{display:flex;gap:8px}
.social span{width:22px;height:22px;border-radius:3px;background:#9a9a9a;display:block}

.rule{top:101px;height:3px;background:var(--grey-line)}
.nav{top:88px;left:636px;font-family:'Open Sans',sans-serif;font-weight:300;font-size:16px;color:#333;display:flex;letter-spacing:.3px}
.nav a{color:inherit;text-decoration:none;position:relative}
.nav a.active{color:var(--green)}
.nav a.active svg{position:absolute;left:20px;top:24px}

.hero{left:101px;top:140px;width:995px;height:265px;background:#f2f2f2;border:1px solid #ddd}
.hero-panel{left:10px;top:7px;width:334px;height:247px;background:radial-gradient(ellipse at 70% 30%,#6cc05a 0%,#42a038 60%,#2f8a2c 100%);color:var(--white);font-family:'Open Sans',sans-serif}
.hero-kicker{left:22px;top:20px;font-size:14.5px;letter-spacing:.2px}
.hero-title{left:40px;top:52px;font-weight:300;font-size:44px;line-height:56px;text-align:right;width:256px}
.hero-arrow{left:200px;top:172px}
.hero-photo{left:344px;top:7px;width:642px;height:247px;background:linear-gradient(120deg,#dfe6ea 0%,#b9c3c8 40%,#8a8f93 65%,#d6dadc 100%)}

.intro-title{left:108px;top:442px;font-family:'Open Sans',sans-serif;font-weight:600;font-size:24.5px;color:var(--green-text)}
.intro-copy{left:106px;top:483px;width:660px;font-style:italic;font-size:13.6px;line-height:20px;color:var(--text)}
.intro-copy p+p{margin-top:20px}
.btn{left:109px;top:636px;width:85px;height:24px;border-radius:3px;background:var(--green);color:var(--white);font-size:12px;font-weight:bold;line-height:24px;padding-left:9px}

.divider{left:110px;top:696px;width:612px;height:1px;background:#bbb}
.story-title{left:110px;top:716px;font-family:'Open Sans',sans-serif;font-weight:600;font-size:16.5px;color:var(--green-text);letter-spacing:.2px}
.story-meta{left:112px;top:748px;font-size:12.5px;color:var(--muted);letter-spacing:.3px}
.story-photo{left:110px;top:778px;width:150px;height:170px;border:3px solid #ccc;background:linear-gradient(#f4f4f4,#d9d9d9 55%,#3a3a40 56%,#2a2a30)}
.story-copy{left:274px;top:774px;width:448px;font-size:13.8px;line-height:22px;color:var(--text);letter-spacing:.3px}
.story-copy p+p{margin-top:22px}

.testimonial{left:797px;top:447px;width:296px;height:215px;border-radius:8px;background:var(--panel)}
.testimonial-tail{left:1012px;top:661px}
.testimonial-title{left:12px;top:15px;font-family:'Cinzel',serif;font-weight:600;font-size:19px;color:var(--green-dark);letter-spacing:.8px}
.testimonial-quote{left:13px;top:52px;width:260px;font-size:14px;line-height:18px;color:var(--text)}
.testimonial-quote .mark{font-family:Georgia,serif;font-size:22px;color:#777;line-height:10px}
.testimonial-author{right:114px;top:157px;font-family:'Open Sans',sans-serif;font-style:italic;font-size:12px;color:#222}
.testimonial-date{right:112px;top:177px;font-family:'Open Sans',sans-serif;font-style:italic;font-size:11.5px;color:#3a8a2e}
.testimonial-avatar{left:201px;top:151px;width:50px;height:42px;background:linear-gradient(#e7c7a4,#c99468)}

.news-band{left:791px;top:721px;width:307px;height:41px;background:var(--green);border-radius:3px 3px 0 0;color:var(--white);font-family:'Open Sans',sans-serif;font-size:23px;line-height:41px;padding-left:18px;letter-spacing:.3px}
.news-tail{left:803px;top:761px}
.news-list{left:791px;top:796px;width:320px;list-style:none}
.news-list li{position:relative;padding-left:18px}
.news-list svg{position:absolute;left:0;top:4px}
.news-date{font-size:12px;color:var(--green-dark)}
.news-text{font-style:italic;font-size:13px;line-height:16px;color:var(--muted)}

.footer{left:0;top:1006px;width:1200px;height:152px;background:linear-gradient(var(--footer-top),var(--footer-bottom))}
.footer-col{top:18px;font-family:'Open Sans',sans-serif;color:var(--white)}
.footer-col h4{font-size:13px;font-weight:600;margin-bottom:5px;letter-spacing:.2px}
.footer-col ul{list-style:none;font-size:11px;line-height:18px;padding-left:1px}
.footer-sep{top:14px;width:1px;height:122px;background:#4b4b4b;box-shadow:1px 0 0 #888}
.copyright{left:0;top:1158px;width:1200px;height:33px;background:var(--footer-bar);color:var(--white);font-size:11px;line-height:30px;text-align:center}
</style>
</head>
<body>

<header>
  <div class="abs brand">
    <span class="brand-dot"></span>
    <span class="brand-name">Bright Harbor Capital</span>
  </div>

  <div class="abs contact">
    <svg width="24" height="22" viewBox="0 0 24 22" aria-hidden="true">
      <path d="M3 14c4 5 9 7 14 6l2-3-4-3-2 2c-3-1-5-3-6-6l2-2-3-4-3 2c-1 3 0 6 0 8z" fill="#6aa84f"/>
      <path d="M13 3a8 8 0 0 1 8 8M13 7a4 4 0 0 1 4 4" stroke="#6aa84f" stroke-width="2" fill="none"/>
    </svg>
    <span class="phone">555-0142-870</span>
    <span class="sep">|</span>
    <span class="follow">Follow us:</span>
    <span class="social" aria-label="Social links">
      <span></span><span></span><span></span><span></span>
    </span>
  </div>

  <div class="abs rule" style="left:0;width:620px"></div>
  <div class="abs rule" style="left:1098px;width:102px"></div>

  <nav class="abs nav">
    <a class="active" href="#" style="margin-right:51px">home
      <svg width="10" height="7" viewBox="0 0 10 7" aria-hidden="true"><path d="M1 1l4 4 4-4" stroke="#4c9e3e" stroke-width="2" fill="none"/></svg>
    </a>
    <a href="#" style="margin-right:51px">about us</a>
    <a href="#" style="margin-right:51px">investment</a>
    <a href="#">entrepreneurs</a>
  </nav>
</header>

<section class="abs hero">
  <div class="abs hero-panel">
    <div class="abs hero-kicker">We're committed to growing businesses</div>
    <div class="abs hero-title">Interested in Funding ?</div>
    <svg class="abs hero-arrow" width="66" height="66" viewBox="0 0 66 66" aria-hidden="true">
      <circle cx="33" cy="33" r="32" fill="#e6e6e6"/>
      <circle cx="33" cy="33" r="26" fill="#3a9a2e"/>
      <path d="M19 30h16v-9l13 12-13 12v-9H19z" fill="#fff"/>
    </svg>
  </div>
  <div class="abs hero-photo" role="img" aria-label="Photo of a business team meeting around a table with laptops"></div>
</section>

<main>
  <h1 class="abs intro-title">Invest with Bright Harbor !</h1>
  <div class="abs intro-copy">
    <p>Many desktop publishing packages and web page editors now use Lorem Ipsum as their default model text, and a search for 'lorem ipsum' will uncover many web sites still in their infancy. Various versions have evolved over the years, sometimes by accident, sometimes on purpose It is a long established fact that a reader will be distracted by the readable content of a page when looking at its layout.</p>
    <p>The point of using Lorem Ipsum is that it has a more-or-less normal distribution of letters, as opposed to using 'Content here, content here', making it look like readable English.</p>
  </div>
  <a class="abs btn" href="#" style="text-decoration:none">read more &raquo;</a>

  <div class="abs divider"></div>

  <h2 class="abs story-title">Through mentoring, strategic advice, expanding network</h2>
  <div class="abs story-meta">GRAIN | 21 January 2014 | Against the grain</div>
  <div class="abs story-photo" role="img" aria-label="Portrait photo of a businessman in a dark suit with arms crossed"></div>
  <div class="abs story-copy">
    <p>when an unknown printer took a galley of type and scrambled it to make a type specimen book. It has survived not only five centuries, but also the leap into electronic typesetting, remaining essentially unchanged. It was popularised in the 1960s with the release of Letterform sheets containing</p>
    <p>Lorem Ipsum passages, and more recently with desktop publishing software like Foliant PageSetter including versions of Lorem Ipsum.</p>
  </div>

  <aside class="abs testimonial">
    <h3 class="abs testimonial-title">Client Testimonials</h3>
    <p class="abs testimonial-quote"><span class="mark">&ldquo;</span> &nbsp;simply dummy text of the printing and typesetting industry. Lorem Ipsum has been the simply dummy text of the printing and typesetting industry. Lorem Ipsum printing &nbsp;<span class="mark">&rdquo;</span></p>
    <div class="abs testimonial-author">By Dale Whitcombe</div>
    <div class="abs testimonial-date">Posted on Nov25, 2013</div>
    <div class="abs testimonial-avatar" role="img" aria-label="Small portrait photo of the client"></div>
  </aside>
  <svg class="abs testimonial-tail" width="44" height="26" viewBox="0 0 44 26" aria-hidden="true"><path d="M0 0h44L0 26z" fill="#e8e8e8"/></svg>

  <div class="abs news-band">Latest News</div>
  <svg class="abs news-tail" width="28" height="16" viewBox="0 0 28 16" aria-hidden="true"><path d="M0 0h28L0 16z" fill="#4c9e3e"/></svg>
  <ul class="abs news-list">
    <li style="margin-bottom:22px"><svg width="13" height="13" viewBox="0 0 13 13" aria-hidden="true"><circle cx="6.5" cy="6.5" r="6" fill="#6ab85a"/><path d="M4 6.5h5M7 4l2.5 2.5L7 9" stroke="#fff" stroke-width="1.5" fill="none"/></svg>
      <div class="news-date">01/15/14</div><div class="news-text">Norvale Goods Acquires Swiftline Quiver</div></li>
    <li style="margin-bottom:14px"><svg width="13" height="13" viewBox="0 0 13 13" aria-hidden="true"><circle cx="6.5" cy="6.5" r="6" fill="#6ab85a"/><path d="M4 6.5h5M7 4l2.5 2.5L7 9" stroke="#fff" stroke-width="1.5" fill="none"/></svg>
      <div class="news-date">01/15/14</div><div class="news-text" style="line-height:18px">simply dummy text of the printing and type setting industry.</div></li>
    <li><svg width="13" height="13" viewBox="0 0 13 13" aria-hidden="true"><circle cx="6.5" cy="6.5" r="6" fill="#6ab85a"/><path d="M4 6.5h5M7 4l2.5 2.5L7 9" stroke="#fff" stroke-width="1.5" fill="none"/></svg>
      <div class="news-date">01/15/14</div><div class="news-text">when an unknown printer took a galley of type and scrambled it to make a type specimen book.</div></li>
  </ul>
</main>

<footer class="abs footer">
  <div class="abs footer-col" style="left:206px"><h4>Home</h4><ul><li>About Us</li><li>Sitemap</li><li>Website Terms</li><li>Terms of Business</li><li>Privacy Policy</li></ul></div>
  <div class="abs footer-sep" style="left:327px"></div>
  <div class="abs footer-col" style="left:364px"><h4>IT Solutions</h4><ul><li>Business Websites</li><li>Reviews</li><li>Quick Tour</li><li>Pricing</li><li>Free Trial</li></ul></div>
  <div class="abs footer-sep" style="left:497px"></div>
  <div class="abs footer-col" style="left:542px"><h4>Investment</h4><ul><li>Marketing Tips</li><li>Search Optimisation</li><li>Social Media</li><li>Video Marketing</li><li>Business Cases</li></ul></div>
  <div class="abs footer-sep" style="left:697px"></div>
  <div class="abs footer-col" style="left:741px"><h4>Web Marketing</h4><ul style="padding-left:5px"><li>Help/Contact us</li><li>Business directory</li><li>Legal notices</li><li>Privacy policy</li><li>Terms &amp; Conditions</li></ul></div>
  <div class="abs footer-sep" style="left:888px"></div>
  <div class="abs footer-col" style="left:916px"><h4>About Us</h4><ul style="padding-left:7px"><li>Blog</li><li>Contact us</li></ul></div>
</footer>
<div class="abs copyright">Copyright &copy; 2014 Bright Harbor Capital Company. All rights reserved.</div>

</body>
</html>
```